dulvox presentation

I would like to improve the presentation of the PoweePoint. That attached.

Target Market(s)

Hotel sector - laboratories - industry

Font styles to use
Other font styles liked:
• como las del diseño

Requirements
Must have
• This PowerPoint. it has to serve as a company presentation.
Nice to have
• I wish it were pleasant to read. with background images or photographs that reinforce the text.

```html
<!DOCTYPE html>
<html lang="ca">
<head>
<meta charset="utf-8">
<title>dulvox – Presentació dels serveis</title>
<link href="https://fonts.googleapis.com/css2?family=Roboto:wght@400;500;700&display=swap" rel="stylesheet">
<style>
:root{
  --blue:#1d4fa8;
  --navy:#0a1f5c;
  --red:#e20f1f;
  --ink:#2f3339;
  --grey:#6f737a;
  --pale:#e8f1fa;
  --light:#eef0f2;
}
*{margin:0;padding:0;box-sizing:border-box}
html,body{width:1200px;height:4441px;overflow:hidden;background:#fff}
body{position:relative;font-family:"Roboto",Arial,sans-serif;color:var(--ink)}
section{position:absolute;left:0;width:1200px;overflow:hidden}
.abs{position:absolute}
.brand{font-weight:700;color:var(--blue);letter-spacing:.06em;white-space:nowrap}
.brand-small{font-size:22px}
.photo{position:absolute}

/* hero */
.hero{top:0;height:716px;background:linear-gradient(100deg,#dcdfe2,#f2f3f4 55%,#eef0f2)}
.hero .gears{left:0;top:0;width:640px;height:716px;background:radial-gradient(circle at 45% 45%,#fbfbfb,#cfd3d7 70%,#e6e8ea)}
.hero .red-bar{right:0;top:0;width:60px;height:716px;background:var(--red)}
.hero .brand{left:620px;top:125px;font-size:96px}
.hero .tagline{left:622px;top:236px;font-size:16px;font-weight:700;color:#3a3d42}
.hero h1{position:absolute;left:619px;top:352px;font-size:31px;font-weight:500;color:var(--blue)}
.hero .intro{left:620px;top:424px;width:440px;font-size:14.5px;line-height:28px;color:var(--grey)}

/* index */
.index{top:716px;height:603px;background:radial-gradient(circle at 75% 45%,#1d55d8,#0b2877 45%,#081a52 80%)}
.index .visual{left:680px;top:30px;width:520px;height:573px;background:radial-gradient(circle at 50% 45%,rgba(70,160,255,.55),rgba(20,70,200,.15) 55%,transparent 75%)}
.index h2{position:absolute;left:143px;top:62px;font-size:30px;font-weight:700;color:#fff}
.index .brand{left:963px;top:65px;color:#fff}
.index ul{position:absolute;left:143px;top:175px;list-style:none;color:#fff;font-size:25px;line-height:42.5px}
.index li{display:flex;align-items:flex-start;gap:22px}
.index li svg{flex:none;margin-top:11px}
.index li.cont{padding-left:48px}

/* areas */
.areas{top:1319px;height:612px;background:#fff}
.title{position:absolute;left:143px;font-size:31px;font-weight:500;line-height:42px;color:#44484e}
.title .b{color:var(--blue)}.title .r{color:var(--red)}
.areas .title{top:70px}
.logo-mark{position:absolute;left:963px}
.lead{position:absolute;left:145px;font-size:14.5px;line-height:28px;color:var(--grey)}
.areas .lead{top:167px}
.areas h3{position:absolute;left:145px;top:240px;font-size:25px;font-weight:500}
.tiles{position:absolute;left:143px;top:314px;display:flex;gap:7px}
.tile{width:222px}
.tile .photo{position:relative;height:189px}
.tile p{text-align:center;margin-top:22px;font-size:15px;font-weight:700}

/* satisfaction */
.satisf{top:1931px;height:945px;background:var(--pale)}
.satisf .title{top:68px}
.satisf .lead{top:186px}
.case{position:absolute;left:145px;width:440px}
.case h4{font-size:25px;font-weight:500;color:#2b2e33}
.case p{margin-top:18px;font-size:14.5px;line-height:28px;color:var(--grey)}
.satisf .worker{left:614px;top:190px;width:586px;height:689px;background:linear-gradient(135deg,#cfd4da,#8a97a8 45%,#3d5f96 70%,#b9c0c8)}
.satisf .curve{position:absolute;left:614px;top:820px}

/* projects */
.projects{top:2876px;height:894px;background:#fff}
.projects .title{top:106px}
.projects .lead{top:203px}
.grid{position:absolute;left:143px;top:281px;display:grid;grid-template-columns:repeat(3,295px);column-gap:16px;row-gap:23px}
.card .photo{position:relative;height:227px}
.card .photo svg{position:absolute;left:0;bottom:0}
.card p{text-align:center;margin-top:9px;font-size:15px;font-weight:700;color:#2b2e33}

/* closing */
.closing{top:3770px;height:671px;background:var(--red)}
.closing .rule{left:0;width:1200px;height:3px;background:var(--blue)}
.closing .panel{left:60px;top:12px;width:1080px;height:659px;background:linear-gradient(160deg,#2156b8,#1a48a3 60%,#2a5fbc)}
.closing .brand{left:0;width:1200px;text-align:center;top:150px;font-size:96px;color:#fff}
.closing .thanks{left:0;width:1200px;text-align:center;top:300px;font-size:29px;font-weight:500;color:var(--red)}
.closing .contact{left:0;width:1200px;text-align:center;top:365px;font-size:20px;line-height:31px;color:#fff}
.closing .gap{height:32px}
</style>
</head>
<body>

<section class="hero">
  <div class="photo gears" role="img" aria-label="White 3D cogwheels on a light grey background"></div>
  <div class="abs red-bar"></div>
  <div class="abs brand">DULVOX</div>
  <div class="abs tagline">REALITZEM I CUIDEM LES TEVES INSTAL·LACIONS</div>
  <h1>PRESENTACIÓ DELS SERVEIS</h1>
  <p class="abs intro">Lorem ipsum dolor sit amet, consectetur adipiscing elit, sed do eiusmod tempor incididunt ut labore et dolore magna aliquauis ipsum suspendisse et dolore magna aliquauis ipsum disse ultrices gravidaisuset dolore magna aliquaui suspendisse ultrices gravidaisusultrices gravidaisus commodoerraecenas accumsan lacus vel facilisis.</p>
</section>

<section class="index">
  <div class="photo visual" role="img" aria-label="Digital hand holding glowing service icons around a wrench and screwdriver"></div>
  <h2>ÍNDEX</h2>
  <div class="abs brand brand-small">DULVOX</div>
  <ul>
    <li><svg width="22" height="22" viewBox="0 0 22 22"><circle cx="11" cy="11" r="9" fill="none" stroke="#fff" stroke-width="2.5"/><path d="M6.5 11.5l3 3 6-6" fill="none" stroke="#fff" stroke-width="2.5"/></svg>Introducció</li>
    <li><svg width="22" height="22" viewBox="0 0 22 22"><circle cx="11" cy="11" r="9" fill="none" stroke="#fff" stroke-width="2.5"/><path d="M6.5 11.5l3 3 6-6" fill="none" stroke="#fff" stroke-width="2.5"/></svg>Les nostres principals àrees d’acció</li>
    <li><svg width="22" height="22" viewBox="0 0 22 22"><circle cx="11" cy="11" r="9" fill="none" stroke="#fff" stroke-width="2.5"/><path d="M6.5 11.5l3 3 6-6" fill="none" stroke="#fff" stroke-width="2.5"/></svg>Instal·lacions amb valor afegit</li>
    <li><svg width="22" height="22" viewBox="0 0 22 22"><circle cx="11" cy="11" r="9" fill="none" stroke="#fff" stroke-width="2.5"/><path d="M6.5 11.5l3 3 6-6" fill="none" stroke="#fff" stroke-width="2.5"/></svg>Anticipar-se. Solucionar. Mantenir</li>
    <li><svg width="22" height="22" viewBox="0 0 22 22"><circle cx="11" cy="11" r="9" fill="none" stroke="#fff" stroke-width="2.5"/><path d="M6.5 11.5l3 3 6-6" fill="none" stroke="#fff" stroke-width="2.5"/></svg>La satisfacció dels nostres clients</li>
    <li class="cont">és el nostre major aval</li>
  </ul>
</section>

<section class="areas">
  <h2 class="title"><span class="b">LES NOSTRES </span><span class="r">PRINCIPALS</span> ÀREES D’ACCIÓ</h2>
  <div class="logo-mark brand brand-small" style="top:76px">DULVOX</div>
  <p class="lead">A DULVOX tenim un leitmotiv que ens acompanya dia rere dia, any rere any:<br>oferir un servei prèmium per a clients selectes</p>
  <h3>Àrees d’acció:</h3>
  <div class="tiles">
    <div class="tile"><div class="photo" role="img" aria-label="Hotel lobby with reception desk" style="background:linear-gradient(135deg,#6f6a60,#b9b6ae 50%,#4b4a46)"></div><p>HOTELS I RESTAURANTS</p></div>
    <div class="tile"><div class="photo" role="img" aria-label="Residence bedroom with bedside table and lamp" style="background:linear-gradient(135deg,#8a6a55,#d9cfc4 55%,#efeae4)"></div><p>RESIDÈNCIES</p></div>
    <div class="tile"><div class="photo" role="img" aria-label="Bright open-plan office with desks" style="background:linear-gradient(135deg,#9aa29c,#e4e7e5 50%,#b8bdb9)"></div><p>OFICINES</p></div>
    <div class="tile"><div class="photo" role="img" aria-label="Shop worker at a coffee counter with yellow wall" style="background:linear-gradient(135deg,#c9a52a,#5a5a5a 55%,#2a2a2a)"></div><p>COMERÇOS</p></div>
  </div>
</section>

<section class="satisf">
  <h2 class="title"><span class="b">SATISFACCIÓ DELS </span><span class="r">NOSTRES CLIENTS</span><br>ÉS EL NOSTRE MAJOR AVAL</h2>
  <div class="logo-mark brand brand-small" style="top:74px">DULVOX</div>
  <p class="lead">A DULVOX estem en constant compromís amb la superació.<br>Aquests són només alguns exemples dels serveis que<br>oferim als nostres clients:</p>
  <div class="case" style="top:296px"><h4>LABORATORIS VERDANEL</h4><p>Legalització i adaptació de les plantes refredadores. Instal·lació d’unitats UTA a la zona packaging.</p></div>
  <div class="case" style="top:436px"><h4>ORVISA</h4><p>Manteniment correctiu i preventiu.</p></div>
  <div class="case" style="top:548px"><h4>HOTEL MIRALDA I HOTEL LUMEN</h4><p>Canvi de sala de calderes de producció semiinstantània.<br>Estalvi previst: 30 % en electricitat i 35 % en gas, segons el projecte d’eficiència energètica.</p></div>
  <div class="case" style="top:717px"><h4>HOTEL SANT FERRAN</h4><p>Canvi de l’antic sistema de calderes amb acumulació per un sistema de producció d’ACS semiinstantani. Fins al moment portem el 38 % d’estalvi en la factura de gas</p></div>
  <div class="photo worker" role="img" aria-label="Technician in blue helmet with laptop beside an electrical panel"></div>
  <svg class="curve" width="586" height="70" viewBox="0 0 586 70"><path d="M0 40 Q290 -10 586 30 L586 70 L0 70Z" fill="#e8f1fa"/><path d="M0 40 Q290 -10 586 30" fill="none" stroke="#1d4fa8" stroke-width="4"/></svg>
</section>

<section class="projects">
  <h2 class="title"><span class="b">LA SATISFACCIÓ DELS </span><span class="r">NOSTRES CLIENTS</span><br>ÉS EL NOSTRE MAJOR AVAL</h2>
  <div class="logo-mark brand brand-small" style="top:112px">DULVOX</div>
  <p class="lead">Alguns dels projectes que hem realitzat a DULVOX:</p>
  <div class="grid">
    <div class="card"><div class="photo" role="img" aria-label="Hotel facade lit at night" style="background:linear-gradient(160deg,#1f2230,#8a7452 55%,#2b2a2e)"><svg width="295" height="26" viewBox="0 0 295 26"><path d="M0 0 Q150 26 295 4 L295 26 L0 26Z" fill="#fff"/><path d="M0 0 Q150 26 295 4" fill="none" stroke="#1d4fa8" stroke-width="3"/></svg></div><p>Hotel Torre Alba, Barcelona</p></div>
    <div class="card"><div class="photo" role="img" aria-label="Restaurant wine cellar with glass table" style="background:linear-gradient(160deg,#151515,#4a4a48 55%,#a9a79f)"><svg width="295" height="26" viewBox="0 0 295 26"><path d="M0 0 Q150 26 295 4 L295 26 L0 26Z" fill="#fff"/><path d="M0 0 Q150 26 295 4" fill="none" stroke="#1d4fa8" stroke-width="3"/></svg></div><p>Restaurant Olmeda, Barcelona</p></div>
    <div class="card"><div class="photo" role="img" aria-label="Modern office with black chair and glass walls" style="background:linear-gradient(160deg,#e6e6e6,#9a9a9a 55%,#2c2c2c)"><svg width="295" height="26" viewBox="0 0 295 26"><path d="M0 0 Q150 26 295 4 L295 26 L0 26Z" fill="#fff"/><path d="M0 0 Q150 26 295 4" fill="none" stroke="#1d4fa8" stroke-width="3"/></svg></div><p>Oficines Nexalia, Barcelona</p></div>
    <div class="card"><div class="photo" role="img" aria-label="Residence room with wooden wall and bed" style="background:linear-gradient(160deg,#4a3328,#7b5a48 55%,#d9d4cf)"><svg width="295" height="26" viewBox="0 0 295 26"><path d="M0 0 Q150 26 295 4 L295 26 L0 26Z" fill="#fff"/><path d="M0 0 Q150 26 295 4" fill="none" stroke="#1d4fa8" stroke-width="3"/></svg></div><p>Residència El Roure, Barcelona</p></div>
    <div class="card"><div class="photo" role="img" aria-label="Cosmetics store entrance" style="background:linear-gradient(160deg,#2a2a2a,#6a6a6a 50%,#b33a3a)"><svg width="295" height="26" viewBox="0 0 295 26"><path d="M0 0 Q150 26 295 4 L295 26 L0 26Z" fill="#fff"/><path d="M0 0 Q150 26 295 4" fill="none" stroke="#1d4fa8" stroke-width="3"/></svg></div><p>Velora, Barcelona</p></div>
    <div class="card"><div class="photo" role="img" aria-label="Illuminated hotel building at dusk" style="background:linear-gradient(160deg,#1c3f8a,#33548f 50%,#8a7a5a)"><svg width="295" height="26" viewBox="0 0 295 26"><path d="M0 0 Q150 26 295 4 L295 26 L0 26Z" fill="#fff"/><path d="M0 0 Q150 26 295 4" fill="none" stroke="#1d4fa8" stroke-width="3"/></svg></div><p>Hotel Brisa 5* GL, Barcelona</p></div>
  </div>
</section>

<section class="closing">
  <div class="abs rule" style="top:0;background:#fff;height:12px"></div>
  <div class="abs rule" style="top:3px"></div>
  <div class="abs rule" style="top:9px;background:var(--red)"></div>
  <div class="abs panel" role="img" aria-label="Faint blue-tinted photo of air-conditioning units"></div>
  <div class="abs brand">DULVOX</div>
  <div class="abs thanks">MOLTES GRÀCIES</div>
  <div class="abs contact">
    Jordi Mas Puigvert<br>Enginyer Industrial I CEO
    <div class="gap"></div>
    +34 600 123 456<br>C. de l'Exemple, 10, 08000 - Barcelona<br>www.dulvox.com
  </div>
</section>

</body>
</html>
```